I would like an amazing design for a eCommerce website called trailhaven.net.

The logo was designed on SketchHive and is attached below. Whatever your design - it MUST use this logo. Please don't waste your time designing new logos.

The logo is on both black and white backgrounds as I've not yet made my mind up whether to ditch "cool black" in favour of more "fresh, clean white"! I'd like to look at both options.

Trail Haven is going to be the first destination of choice for anyone who is bored or frustrated at home and wants a life full of adventure. It will stock outdoor clothing and equipment, training kit, expedition gear, and travel clothing and accessories.

But it is a very cool place to go. A fun and exciting Aladdin's cave full of fantastic adventure kit. We will stock inflatable pack rafts, machetes, hammocks and other expedition gear as well as standard outdoor clothing.

This is NOT a geeky outdoor store selling pac-a-macs and walking poles.

The unique thing is that everything stocked is hand selected by me, Tom Bexley, an experienced explorer who became the first person to walk the Amazon in 2010. tombexley.net is my site. I now make TV for Horizon Network.

There will be items at every price level from "only the best" - absolute top end kit, to "get the job done" - stuff that won't break the bank. Everything stocked works. If it doesn't - I won't sell it.

So although the theme is fun and adventurous I have to have it also feeling like a place of professional, expert advice. A place of substance and depth.

Thanks in advance for all your ideas and designs!

Best
Tom
Updates

The designs that I like the best have used jungle images as background wallpaper - possible with a green tint to them so that they really do look like background rather than the focus. The focus should obviously be the kit for sale. The best designs have this on a fresh white or light grey background so that it stands out. I like the main logo being in a black header and footer. But the feel of the site can easily become too dark if too much back is used or if the green background image is too dark. We want adventure and cool - but it has to feel light and professional enough to be accessible by people of all ages. Most websites that are successful are white after all and whilst I'd like to be a bit more adventurous than that we shouldn't over do the darkness!

I'm not really a massive fan of side bars and would hope that whichever site I chose had a mega menu system like Corwin Latch that could navigate quickly and easily to any item intuitively.

Any sliders must be about selling kit not images of me.

Thanks so much to everyone who has submitted designs - there are some VERY cool ones out there at the moment

Best,
Tom

Target Market(s)

The target market is primarily 16 to 50 years old outdoor enthusiasts however I will be selling to older people and kids, male and female, so it can't be too modern, too macho, or too complicated to put anyone off.

Requirements
Must have
• Bold, professional, adventurous feel. Not cluttered but not so minimalist that it looks boring too. I would like to select a few colours and work with them.
• Red for high lighted emphasis. See logo
• Greens/blacks/greys as background.
• Clean menu system. I'm probably going use a tailored version of http://plumtide-theme.shopsample.net with mega menus.
Nice to have
• Some personalisation that makes the site mine. Use of hi res images below as background could work although I am keen for the site to look clean and easy to navigate.
Should not have
• Hundreds of boxes and text and clutter. I want this site to show off the items in a classy manner. This is NOT gear barn.net! This is a site where hand selected items are proudly displayed and put together, after a lot of thought.

```html
<!DOCTYPE html>
<html lang="en">
<head>
<meta charset="utf-8">
<title>Trail Haven — Home</title>
<link rel="stylesheet" href="https://fonts.googleapis.com/css2?family=Montserrat:wght@500;700;800&family=Questrial&display=swap">
<style>
  :root{
    --black:#000;
    --ink:#111;
    --white:#fff;
    --red:#c4161c;
    --red-deep:#5a0a0c;
    --maroon:#3a0608;
    --rust:#6b1a10;
    --pink:#e0356f;
    --salmon:#f08a7a;
    --amber:#f2a51f;
    --rose:#ef5b8c;
    --grey:#8c8c8c;
    --field:#9a9a9a;
    --text-muted:#cfcfcf;
    --sans:"Questrial", "Century Gothic", sans-serif;
    --bold:"Montserrat", Arial, sans-serif;
  }
  *{box-sizing:border-box;margin:0;padding:0}
  html,body{width:933px;height:1200px;overflow:hidden;background:var(--black)}
  body{position:relative;font-family:var(--sans);color:var(--white)}
  .abs{position:absolute}

  /* header */
  .site-header{left:0;top:0;width:933px;height:70px;background:var(--black)}
  .brand{left:83px;top:18px}
  .brand-name{font-family:var(--bold);font-weight:800;font-size:23px;letter-spacing:1px;color:var(--red);text-transform:uppercase;line-height:1;white-space:nowrap}
  .brand-tag{font-size:10px;color:var(--white);margin-top:3px;letter-spacing:.3px;white-space:nowrap}
  .account{left:655px;top:18px;font-size:12px;color:var(--white);white-space:nowrap}
  .account .sep{color:var(--red)}
  .cart-btn{left:762px;top:16px;width:86px;height:24px;border-radius:12px;background:linear-gradient(#f25b8f,var(--pink));border:2px solid #fbd0df;display:flex;align-items:center;padding-left:1px;font-family:var(--bold);font-weight:700;font-size:10px;color:var(--white);white-space:nowrap}
  .cart-btn .cart-icon{flex:none;width:18px;height:18px;border-radius:50%;background:var(--white);margin-right:8px;display:flex;align-items:center;justify-content:center}

  /* nav */
  .main-nav{left:0;top:71px;width:933px;height:22px;background:var(--white)}
  .main-nav a{position:absolute;top:5px;font-size:11px;color:var(--ink);text-decoration:none;text-transform:uppercase;letter-spacing:.3px;white-space:nowrap}
  .main-nav a.active{color:var(--red)}
  .search-label{left:667px;top:5px;font-size:11px;color:var(--ink);font-weight:700;font-family:var(--bold)}
  .search-field{left:721px;top:3px;width:131px;height:16px;border-radius:8px;background:var(--field)}

  /* hero */
  .hero-photo{left:207px;top:107px;width:513px;height:193px;background:linear-gradient(160deg,#5d4a35,#3e3a28 45%,#6e6e60);border:3px solid var(--white)}
  .slider-arrow{top:175px;width:38px;height:62px;background:var(--red);display:flex;align-items:center;justify-content:center}
  .slider-arrow.prev{left:203px;border-radius:0 31px 31px 0}
  .slider-arrow.next{left:685px;border-radius:31px 0 0 31px}

  .intro{left:116px;top:367px;width:696px;height:180px}
  .intro-portrait{left:180px;top:380px;width:134px;height:134px;border-radius:50%;background:radial-gradient(circle at 45% 40%,#c99a7c,#8c6650 70%);border:4px solid #e6e6e6}
  .intro-text{left:353px;top:385px;width:430px;font-style:italic;font-size:9.6px;line-height:16.4px;text-transform:uppercase;color:var(--ink);letter-spacing:.2px}

  /* featured */
  .featured-bg{left:0;top:573px;width:933px;height:470px;background:radial-gradient(ellipse at 30% 40%,#4a0a0c,var(--maroon) 40%,#150203 85%)}
  .featured-title{left:160px;top:624px;width:613px;text-align:center;font-family:var(--bold);font-weight:700;font-size:19px;color:var(--ink);letter-spacing:.5px}
  .product{top:660px;width:182px}
  .product-head{position:relative;height:33px;background:var(--red);font-family:var(--bold);font-weight:700;font-size:13px;text-align:center;line-height:33px;color:var(--white);text-transform:uppercase}
  .product-head::after{content:"";position:absolute;right:0;top:0;border-style:solid;border-width:0 33px 33px 0;border-color:transparent var(--corner) transparent transparent}
  .product-photo{margin:0 8px;height:160px}
  .product-desc{margin:22px -14px 0;font-family:var(--bold);font-weight:700;font-size:7px;line-height:11px;text-align:center;color:var(--ink);text-transform:uppercase;white-space:nowrap}
  .quick-view{display:block;margin:6px auto 0;width:100px;height:23px;border-radius:12px;background:var(--black);font-family:var(--bold);font-weight:700;font-size:10.5px;line-height:23px;text-align:center;color:var(--white);text-transform:uppercase;white-space:nowrap}

  /* footer */
  .site-footer{left:0;top:1027px;width:933px;height:173px;background:var(--black)}
  .footer-col h4{font-family:var(--sans);font-style:italic;font-weight:700;font-size:12px;text-decoration:underline;color:var(--white);margin-bottom:10px;white-space:nowrap}
  .quick-links li{list-style:none;font-size:8px;line-height:11.5px;font-style:italic;text-transform:uppercase;padding-left:8px}
  .social li{list-style:none;display:flex;align-items:center;font-size:12px;font-style:italic;color:var(--grey);height:22px}
  .social .ico{width:15px;height:15px;background:#4a4a4a;margin-right:8px}
  .contact li{list-style:none;display:flex;align-items:center;font-size:15px;height:26px;white-space:nowrap}
  .contact li.mail{font-size:13px;font-style:italic}
  .contact svg{margin-right:10px}
  .footer-brand{left:649px;top:1104px}
  .footer-brand .brand-name{color:var(--white);font-size:16px}
  .footer-brand .brand-tag{font-size:7px;color:var(--grey)}
  .copyright{left:0;top:1180px;width:795px;text-align:center;font-size:7.5px;color:var(--white)}
</style>
</head>
<body>

<header class="site-header abs">
  <div class="brand abs">
    <div class="brand-name">Trail Haven</div>
    <div class="brand-tag">Everything for a life of adventure - by Tom Bexley</div>
  </div>
  <div class="account abs">Log in <span class="sep">or</span> Sign up</div>
  <div class="cart-btn abs">
    <span class="cart-icon">
      <svg width="12" height="11" viewBox="0 0 12 11"><path d="M0 1h2l2 6h6l1.5-4.5H3" fill="none" stroke="#e0356f" stroke-width="1.4"/><circle cx="5" cy="9.5" r="1" fill="#e0356f"/><circle cx="9" cy="9.5" r="1" fill="#e0356f"/></svg>
    </span>View cart
  </div>
</header>

<nav class="main-nav abs">
  <a class="active" style="left:133px" href="#">Home</a>
  <a style="left:191px" href="#">About us</a>
  <a style="left:268px" href="#">Adventure</a>
  <a style="left:356px" href="#">Shop</a>
  <a style="left:411px" href="#">Blog</a>
  <a style="left:466px" href="#">Contact</a>
  <span class="search-label abs">SEARCH</span>
  <span class="search-field abs">
    <svg class="abs" style="right:6px;top:2px" width="12" height="12" viewBox="0 0 12 12"><circle cx="5" cy="5" r="3.6" fill="none" stroke="#fff" stroke-width="1.6"/><path d="M7.6 7.6l3.4 3.4" stroke="#fff" stroke-width="1.8"/></svg>
  </span>
</nav>

<section class="hero">
  <div class="hero-photo abs" role="img" aria-label="Slider photo: explorer wading through a flooded jungle with expedition gear"></div>
  <svg class="abs" style="left:116px;top:296px" width="696" height="75" viewBox="0 0 696 75" role="img" aria-label="Muddy river water spilling out of the slider frame">
    <defs><linearGradient id="water" x1="0" y1="0" x2="0" y2="1"><stop offset="0" stop-color="#9c9c9c"/><stop offset="1" stop-color="#5a5a5a"/></linearGradient></defs>
    <path d="M91 4H604L696 64V75H0V64Z" fill="url(#water)"/>
  </svg>
  <div class="slider-arrow prev abs"><svg width="16" height="26" viewBox="0 0 16 26"><path d="M13 3L4 13l9 10" fill="none" stroke="#fff" stroke-width="4"/></svg></div>
  <div class="slider-arrow next abs"><svg width="16" height="26" viewBox="0 0 16 26"><path d="M3 3l9 10-9 10" fill="none" stroke="#fff" stroke-width="4"/></svg></div>

  <svg class="intro abs" viewBox="0 0 696 180" preserveAspectRatio="none">
    <path d="M0 0H696V168L655 157 580 173 520 160 440 170 370 157 300 172 220 160 150 170 60 156 0 165Z" fill="#4a1a0d"/>
    <path d="M0 0H696V158L655 150 580 165 520 152 440 162 370 150 300 164 220 152 150 162 60 148 0 156Z" fill="#fff"/>
  </svg>
  <div class="intro-portrait abs" role="img" aria-label="Portrait of Tom Bexley laughing"></div>
  <p class="intro-text abs">Lorem Ipsum is simply dummy text of the printing and typesetting industry. Lorem Ipsum has been the industry's standard dummy text ever since the 1500s, when an unknown printer took a galley of type and scrambled it to make a type specimen book. It has survived not only five centuries, but also the leap into electronic typesetting, remaining essentially unchanged. It was popularised in the 1960s with the release of Lettramark sheets containing Lorem Ipsum passages, and more recently with desktop publishing software like Pageforge including versions of Lorem Ipsum.</p>
</section>

<section class="featured">
  <div class="featured-bg abs"></div>
  <svg class="abs" style="left:0;top:573px" width="933" height="470" viewBox="0 0 933 470">
    <path d="M160 48L215 30 300 42 380 16 470 38 560 20 640 34 700 10 773 22 770 200 778 400 700 388 640 402 560 380 470 398 390 382 300 400 220 384 160 396Z" fill="#fff"/>
    <path d="M0 455L70 430 140 440 240 425 330 442 420 428 520 440 610 422 700 436 790 424 870 438 933 420V470H0Z" fill="#fff"/>
  </svg>
  <h2 class="featured-title abs">FEATURED ITEMS</h2>

  <article class="product abs" style="left:171px;--corner:var(--salmon)">
    <div class="product-head">Lorem Ipsum</div>
    <div class="product-photo" role="img" aria-label="Product photo: explorer climbing through jungle undergrowth" style="background:linear-gradient(150deg,#3d6b2a,#1e3516 60%,#6c8f4a)"></div>
    <p class="product-desc">Lorem Ipsum is simply dummy text of the<br>printing and typesetting industry.</p>
    <span class="quick-view">Quick view</span>
  </article>

  <article class="product abs" style="left:369px;--corner:var(--amber)">
    <div class="product-head">Lorem Ipsum</div>
    <div class="product-photo" role="img" aria-label="Product photo: explorer in a cap carrying a backpack in the forest" style="background:linear-gradient(150deg,#4b6b3a,#2b3a22 60%,#7a8c5a)"></div>
    <p class="product-desc">Lorem Ipsum is simply dummy text of the<br>printing and typesetting industry.</p>
    <span class="quick-view">Quick view</span>
  </article>

  <article class="product abs" style="left:571px;--corner:var(--rose)">
    <div class="product-head">Lorem Ipsum</div>
    <div class="product-photo" role="img" aria-label="Product photo: explorer with a red rucksack holding a machete in the jungle" style="background:linear-gradient(150deg,#6d8f4c,#3a5a2a 55%,#a0b27a)"></div>
    <p class="product-desc">Lorem Ipsum is simply dummy text of the<br>printing and typesetting industry.</p>
    <span class="quick-view">Quick view</span>
  </article>
</section>

<footer class="site-footer abs">
  <div class="footer-col abs" style="left:195px;top:40px">
    <h4>Quick Links</h4>
    <ul class="quick-links">
      <li>Home</li><li>About us</li><li>Adventure</li><li>Shop</li><li>Blog</li><li style="margin-top:4px">Contact</li>
    </ul>
  </div>
  <div class="footer-col abs" style="left:365px;top:40px">
    <h4>Connect With Us</h4>
    <ul class="social">
      <li><span class="ico"></span>Friendwall</li>
      <li><span class="ico"></span>Chirpline</li>
      <li><span class="ico"></span>Streamcast</li>
    </ul>
  </div>
  <div class="footer-col abs" style="left:493px;top:40px">
    <h4>Contact Us</h4>
    <ul class="contact">
      <li><svg width="18" height="18" viewBox="0 0 18 18"><circle cx="9" cy="9" r="8" fill="none" stroke="#fff" stroke-width="1.4"/><path d="M6 5l2 2-1 1.5c.7 1.2 1.3 1.8 2.5 2.5L11 10l2 2-1.2 1.3C9 13 5.5 9.5 5 6.2Z" fill="#fff"/></svg>555-014-277</li>
      <li class="mail"><svg width="18" height="13" viewBox="0 0 18 13"><rect x="1" y="1" width="16" height="11" fill="none" stroke="#fff" stroke-width="1.3"/><path d="M1 1l8 6 8-6" fill="none" stroke="#fff" stroke-width="1.3"/></svg>trailhaven.net</li>
    </ul>
  </div>
  <div class="footer-brand abs" style="top:77px">
    <div class="brand-name">Trail Haven</div>
    <div class="brand-tag">Everything for a life of adventure - by Tom Bexley</div>
  </div>
  <p class="copyright abs" style="top:153px">copyright@trailhaven.net</p>
</footer>

</body>
</html>
```